Looking for a website design for my company
Services we offer:
Phone Repair
TV Mounting
Security Camera Installation
Networking / Wi-Fi
Smart Home Services
IT Support

Looking for a website similar to qarnel.com

Few tabs
About Us
Contact Us
Areas Served
Pricing and Services

```html
<!DOCTYPE html>
<html lang="en">
<head>
<meta charset="utf-8">
<title>Vanto Rim – Repair &amp; Installation</title>
<link href="https://fonts.googleapis.com/css2?family=Lato:wght@400;700;900&family=Source+Sans+3:wght@400;600;700&display=swap" rel="stylesheet">
<style>
:root{
  --orange:#f7931e;
  --orange-dark:#e5820f;
  --ink:#1e1e1e;
  --text:#444;
  --muted:#777;
  --line:#e4e4e4;
  --grey-bg:#f1f1f1;
  --footer:#141414;
  --footer-text:#d9d9d9;
  --white:#fff;
}
*{margin:0;padding:0;box-sizing:border-box}
html,body{width:1200px;height:3991px;overflow:hidden}
body{position:relative;font-family:"Lato",sans-serif;color:var(--text);background:var(--white)}
.abs{position:absolute}
.heading{font-family:"Source Sans 3",sans-serif;font-weight:600;color:var(--ink)}
.photo{position:absolute}

/* header */
.topbar{position:absolute;left:0;top:0;width:1200px;height:83px;background:var(--white)}
.logo-panel{position:absolute;left:0;top:0;width:365px;height:83px;background:#f4f4f4;clip-path:polygon(0 0,100% 0,92% 100%,0 100%)}
.logo{position:absolute;left:90px;top:14px;display:flex;align-items:center;gap:10px;font-family:"Source Sans 3",sans-serif;font-weight:700;font-size:46px;color:var(--orange);line-height:52px}
.logo-mark{width:16px;height:16px;background:var(--orange)}
.contact-box{position:absolute;top:18px;display:flex;align-items:center;gap:16px}
.contact-icon{width:44px;height:44px;border:2px solid var(--orange);border-radius:50%;display:flex;align-items:center;justify-content:center}
.contact-label{font-size:13px;color:var(--muted);line-height:18px}
.contact-value{font-size:15px;font-weight:700;color:var(--ink);line-height:22px}
.contact-value.light{font-weight:400;color:var(--muted);font-size:14px}
.navbar{position:absolute;left:0;top:83px;width:1200px;height:47px;background:var(--orange)}
.nav-item{position:absolute;top:14px;font-size:16px;font-weight:700;color:var(--white)}
.nav-item.active{color:var(--ink)}
.nav-item.active::after{content:"";position:absolute;left:0;right:0;bottom:-12px;height:3px;background:var(--ink)}
.nav-social{position:absolute;top:17px;width:14px;height:14px;border-radius:50%;background:#fbd4a3}

/* hero */
.hero{position:absolute;left:0;top:130px;width:1200px;height:523px;background:linear-gradient(100deg,#e9eaec 0%,#dcdde0 40%,#8d8a88 70%,#6f6b69 100%)}
.hero-title{position:absolute;left:88px;top:215px;font-family:"Lato",sans-serif;font-weight:900;font-size:68px;color:var(--ink);letter-spacing:-0.5px}
.hero-sub{position:absolute;left:88px;top:300px;font-size:28px;color:var(--ink)}
.btn{position:absolute;background:var(--orange);color:var(--white);border-radius:30px;font-weight:700;display:flex;align-items:center;justify-content:center}
.hero-btn{left:90px;top:366px;width:197px;height:53px;font-size:20px}
.dot{position:absolute;top:537px;width:12px;height:12px;border-radius:50%;background:#9a9a9a}
.dot.on{background:var(--orange)}

/* services row */
.service{position:absolute;top:693px;width:180px;text-align:center;font-size:15px;line-height:22px;color:var(--muted)}
.service svg{display:block;margin:0 auto 14px}
.service-divider{position:absolute;top:698px;width:1px;height:105px;background:var(--line)}

/* specialized */
.section-title{position:absolute;left:0;width:1200px;text-align:center;font-size:41px}
.spec-card{position:absolute;top:972px;width:334px;height:240px;display:flex;flex-direction:column;align-items:center;justify-content:center;gap:10px}
.spec-card span{font-family:"Source Sans 3",sans-serif;font-weight:700;font-size:25px;color:var(--white);margin-top:4px}

/* about */
.about{position:absolute;left:0;top:1299px;width:1200px;height:499px;background:var(--grey-bg)}
.about-title{position:absolute;left:90px;top:1385px;font-size:40px}
.about-text{position:absolute;left:90px;top:1455px;width:485px;font-size:15.5px;line-height:29.5px;color:var(--text)}

/* testimonials */
.t-card{position:absolute;top:1945px;width:290px;height:377px;background:var(--white);box-shadow:0 3px 12px rgba(0,0,0,.09)}
.t-photo{position:absolute;left:0;top:0;width:100%;height:282px}
.t-quote{position:absolute;left:17px;bottom:16px;right:14px;font-size:15px;line-height:26px;color:var(--white)}
.t-avatar{position:absolute;left:9px;top:301px;width:40px;height:40px;border-radius:50%;background:#c9a48a}
.t-name{position:absolute;left:63px;top:301px;font-size:15px;color:var(--ink)}
.t-place{position:absolute;left:63px;top:321px;font-size:13px;font-style:italic;color:var(--muted)}
.t-date{position:absolute;left:9px;top:357px;font-size:10.5px;color:var(--muted)}
.arrow-btn{position:absolute;top:2136px}

/* ready */
.ready{position:absolute;left:0;top:2412px;width:1200px;height:499px;background:var(--grey-bg)}
.ready-title{position:absolute;left:676px;top:2535px;font-size:39px;line-height:50px;font-weight:400}
.ready-text{position:absolute;left:676px;top:2656px;font-size:15px;color:var(--ink)}
.ready-btn{left:677px;top:2727px;width:165px;height:48px;font-size:14px}

/* blog */
.blog-img{position:absolute;top:3053px;width:329px;height:244px}
.blog-title{position:absolute;top:3316px;width:335px;font-family:"Source Sans 3",sans-serif;font-weight:700;font-size:24.5px;line-height:31px;color:var(--ink)}
.blog-rule{position:absolute;width:30px;height:3px;background:var(--orange)}
.blog-text{position:absolute;width:320px;font-size:13.5px;line-height:26px;color:var(--text)}
.read-more{position:absolute;font-size:14px;font-weight:700;color:var(--orange)}

/* footer */
.footer{position:absolute;left:0;top:3577px;width:1200px;height:414px;background:var(--footer)}
.f-head{position:absolute;top:3639px;font-family:"Lato",sans-serif;font-weight:700;font-size:17px;color:var(--white);letter-spacing:.3px}
.f-small{position:absolute;font-size:12px;line-height:20px;color:var(--footer-text)}
.news-thumb{position:absolute;width:70px;height:57px;background:linear-gradient(135deg,#8a6a52,#2c2c2c)}
.news-date{font-size:9.5px;font-weight:700}
.f-link{position:absolute;left:367px;font-size:12px;color:var(--footer-text)}
.f-input{position:absolute;left:569px;top:3751px;width:202px;height:48px;background:var(--white);font-size:12px;color:#888;padding:16px 14px}
.f-send{position:absolute;left:773px;top:3751px;width:45px;height:48px;background:var(--orange);display:flex;align-items:center;justify-content:center}
.f-social{position:absolute;top:3827px;width:12px;height:12px;border-radius:50%;background:#666}
.f-rule{position:absolute;left:873px;width:240px;height:1px;background:#333}
.f-row{position:absolute;left:873px;display:flex;align-items:flex-start;gap:10px;font-size:12px;line-height:20px;color:var(--footer-text)}
.f-row svg{margin-top:3px;flex:none}
.copyright{position:absolute;left:0;top:3962px;width:1200px;text-align:center;font-size:11.5px;color:var(--white)}
</style>
</head>
<body>

<header class="topbar">
  <div class="logo-panel"></div>
  <div class="logo"><span class="logo-mark"></span>Vanto Rim</div>
  <div class="contact-box" style="left:687px">
    <div class="contact-icon"><svg width="18" height="18" viewBox="0 0 24 24"><path d="M6.6 10.8a15 15 0 0 0 6.6 6.6l2.2-2.2a1 1 0 0 1 1-.25 11.4 11.4 0 0 0 3.6.57 1 1 0 0 1 1 1V20a1 1 0 0 1-1 1A17 17 0 0 1 3 4a1 1 0 0 1 1-1h3.5a1 1 0 0 1 1 1c0 1.25.2 2.45.57 3.57a1 1 0 0 1-.25 1z" fill="#f7931e"/></svg></div>
    <div><div class="contact-label">Call Now:</div><div class="contact-value">555-014-2280</div></div>
  </div>
  <div class="contact-box" style="left:927px">
    <div class="contact-icon"><svg width="18" height="14" viewBox="0 0 18 14"><rect x="0" y="0" width="18" height="14" rx="2" fill="#f7931e"/><path d="M1 1.5l8 6 8-6" stroke="#fff" stroke-width="1.6" fill="none"/></svg></div>
    <div><div class="contact-label">Email:</div><div class="contact-value light">info@vantorim.com</div></div>
  </div>
</header>

<nav class="navbar">
  <span class="nav-item active" style="left:102px">Home</span>
  <span class="nav-item" style="left:203px">About Us</span>
  <span class="nav-item" style="left:330px">Areas Served</span>
  <span class="nav-item" style="left:490px">Pricing and Services</span>
  <span class="nav-item" style="left:708px">Contact Us</span>
  <span class="nav-social" style="left:982px"></span>
  <span class="nav-social" style="left:1019px"></span>
  <span class="nav-social" style="left:1060px"></span>
</nav>

<section class="hero" role="img" aria-label="Technician installing a ceiling security camera"></section>
<h1 class="hero-title">Vanto Rim</h1>
<p class="hero-sub">Lorem ipsum dolor sit amet, consectetur</p>
<a class="btn hero-btn">Get Started</a>
<span class="dot on" style="left:91px"></span>
<span class="dot" style="left:115px"></span>
<span class="dot" style="left:139px"></span>
<span class="dot" style="left:163px"></span>

<div class="service" style="left:42px">
  <svg width="40" height="50" viewBox="0 0 40 50" fill="none" stroke="#999" stroke-width="2"><rect x="6" y="2" width="28" height="46" rx="3"/><circle cx="22" cy="26" r="6"/><line x1="16" y1="43" x2="24" y2="43"/></svg>
  Phone<br>Repair</div>
<div class="service-divider" style="left:226px"></div>
<div class="service" style="left:229px">
  <svg width="66" height="50" viewBox="0 0 66 50" fill="none" stroke="#999" stroke-width="2"><rect x="18" y="6" width="30" height="38"/><rect x="4" y="12" width="10" height="26"/><rect x="52" y="12" width="10" height="26"/><line x1="14" y1="20" x2="18" y2="20"/><line x1="14" y1="30" x2="18" y2="30"/><line x1="48" y1="20" x2="52" y2="20"/><line x1="48" y1="30" x2="52" y2="30"/></svg>
  TV<br>Mounting</div>
<div class="service-divider" style="left:414px"></div>
<div class="service" style="left:417px">
  <svg width="56" height="50" viewBox="0 0 56 50" fill="none" stroke="#999" stroke-width="2"><rect x="4" y="2" width="14" height="10"/><path d="M11 12v8h30"/><rect x="20" y="16" width="28" height="30" rx="12"/><circle cx="34" cy="31" r="7"/><circle cx="34" cy="31" r="3"/></svg>
  Security Camera<br>Installation</div>
<div class="service-divider" style="left:602px"></div>
<div class="service" style="left:604px">
  <svg width="56" height="50" viewBox="0 0 56 50" fill="none" stroke="#999" stroke-width="2"><rect x="10" y="8" width="36" height="26" rx="2"/><path d="M4 40h48l-4 6H8z"/><path d="M20 20a11 11 0 0 1 16 0M23 24a6 6 0 0 1 10 0"/><circle cx="28" cy="28" r="1.5" fill="#999"/></svg>
  Networking /<br>Wi-Fi</div>
<div class="service-divider" style="left:788px"></div>
<div class="service" style="left:792px">
  <svg width="54" height="50" viewBox="0 0 54 50" fill="none" stroke="#999" stroke-width="2"><path d="M6 24L27 6l21 18"/><path d="M12 20v26h30V20"/><rect x="21" y="26" width="12" height="12"/><line x1="27" y1="26" x2="27" y2="38"/><line x1="21" y1="32" x2="33" y2="32"/><path d="M38 6a8 8 0 0 1 8 8"/></svg>
  Smart Home<br>Services</div>
<div class="service-divider" style="left:983px"></div>
<div class="service" style="left:978px">
  <svg width="50" height="50" viewBox="0 0 50 50" fill="none" stroke="#999" stroke-width="2"><rect x="4" y="4" width="42" height="30" rx="2"/><line x1="25" y1="34" x2="25" y2="42"/><line x1="14" y1="44" x2="36" y2="44"/><circle cx="25" cy="17" r="6"/></svg>
  IT<br>Support</div>

<h2 class="section-title heading" style="top:902px">We are specialized in</h2>
<div class="spec-card" style="left:90px;background:linear-gradient(135deg,#a9a6a2,#5f5852)" role="img" aria-label="Woman controlling a smart home tablet">
  <svg width="56" height="52" viewBox="0 0 56 52" fill="none" stroke="#fff" stroke-width="2.5"><path d="M4 26L28 6l24 20"/><path d="M11 21v27h34V21"/><rect x="22" y="28" width="12" height="12"/><path d="M38 4a10 10 0 0 1 10 10"/></svg>
  <span>Smart Home</span></div>
<div class="spec-card" style="left:432px;background:linear-gradient(135deg,#8c8c90,#3a3a40)" role="img" aria-label="Technician repairing a phone circuit board">
  <svg width="56" height="52" viewBox="0 0 56 52" fill="none" stroke="#fff" stroke-width="2.5"><path d="M8 44L40 12"/><path d="M36 6l10 10 4-4-10-10z"/><path d="M8 8l36 36"/><circle cx="10" cy="10" r="6"/><rect x="38" y="38" width="10" height="10" transform="rotate(45 43 43)"/></svg>
  <span>Repair Industry</span></div>
<div class="spec-card" style="left:775px;background:linear-gradient(135deg,#40486a,#1c1f2c)" role="img" aria-label="Installer mounting a wall screen">
  <svg width="56" height="52" viewBox="0 0 56 52" fill="none" stroke="#fff" stroke-width="2.5"><circle cx="32" cy="16" r="8"/><circle cx="32" cy="16" r="13" stroke-dasharray="4 3"/><path d="M4 34h10l8 6h14a4 4 0 0 1 0 8H14"/><path d="M36 44l14-8"/></svg>
  <span>Installation</span></div>

<section class="about"></section>
<div class="photo" style="left:614px;top:1299px;width:586px;height:499px;background:linear-gradient(120deg,#8fa3aa,#dfe4e6 50%,#b9a391)" role="img" aria-label="Hands adjusting a white dome security camera"></div>
<h2 class="about-title heading">About Us</h2>
<p class="about-text">Lorem ipsum dolor sit amet, consectetur adipiscing elit, sed do eiusmod tempor incididunt ut labore et dolore magna aliqua. Ut enim ad minim veniam, quis nostrud exercitation ullamco laboris nisi ut aliquip ex ea commodo consequat. Duis aute irure dolor in reprehenderit in voluptate velit esse cillum dolore eu fugiat nulla pariatur. Excepteur sint occaecat cupidatat non proident, sunt in culpa qui officia deserunt mollit anim id est laborum</p>
<svg class="abs" style="left:90px;top:1688px" width="40" height="12" viewBox="0 0 40 12"><line x1="0" y1="6" x2="38" y2="6" stroke="#333" stroke-width="1.5"/><path d="M32 1l6 5-6 5" stroke="#333" stroke-width="1.5" fill="none"/></svg>

<h2 class="section-title heading" style="top:1872px">Testimonials</h2>
<svg class="arrow-btn" style="left:79px" width="12" height="16" viewBox="0 0 12 16"><path d="M9 2L3 8l6 6" stroke="#555" stroke-width="1.6" fill="none"/></svg>
<svg class="arrow-btn" style="left:1110px" width="12" height="16" viewBox="0 0 12 16"><path d="M3 2l6 6-6 6" stroke="#555" stroke-width="1.6" fill="none"/></svg>

<article class="t-card" style="left:141px">
  <div class="t-photo" style="background:linear-gradient(135deg,#b08766,#6e4b32 60%,#c9892b)" role="img" aria-label="Living room wall with smart home control overlay">
    <p class="t-quote">“Lorem ipsum dolor sit amet, consectetur adipiscing elit, sed do eiusmod tempor incididunt ut labore et dolore magna aliqua.”</p>
  </div>
  <div class="t-avatar"></div><div class="t-name">Marlo T.</div><div class="t-place">Duluth, GA</div>
  <div class="t-date">Added on 01/21/2020 09:27:24 pm</div>
</article>
<article class="t-card" style="left:453px;width:296px">
  <div class="t-photo" style="background:linear-gradient(135deg,#6a5c4e,#3c3129 60%,#8d7a66)" role="img" aria-label="Hand holding a phone near a wireless router">
    <p class="t-quote">“Lorem ipsum dolor sit amet, consectetur adipiscing elit, sed do”</p>
  </div>
  <div class="t-avatar"></div><div class="t-name">Dorian K.</div><div class="t-place">North Las Vegas, NV</div>
  <div class="t-date">Added on 01/21/2020 09:19:30 pm</div>
</article>
<article class="t-card" style="left:770px">
  <div class="t-photo" style="background:linear-gradient(135deg,#8a6a4c,#3b3129 60%,#5b6066)" role="img" aria-label="Two colleagues smiling at a computer">
    <p class="t-quote">“Lorem ipsum dolor sit amet, consectetur adipiscing elit, sed do eiusmod tempor incididunt ut labore et dolore magna aliqua.”</p>
  </div>
  <div class="t-avatar" style="background:#8aa0b8"></div><div class="t-name">Elias M.</div><div class="t-place">Flagstaff, AZ</div>
  <div class="t-date">Added on 01/21/2020 09:03:06 pm</div>
</article>

<section class="ready"></section>
<div class="photo" style="left:0;top:2412px;width:586px;height:499px;background:linear-gradient(180deg,#e4e4e2 0%,#d9d8d4 55%,#2c3f78 75%,#d8d6d1 100%)" role="img" aria-label="Couple relaxing on a blue sofa in a bright living room"></div>
<h2 class="ready-title heading">Ready to get<br>started?</h2>
<p class="ready-text">Repair or install a device today.</p>
<a class="btn ready-btn">Book a Services</a>

<h2 class="section-title heading" style="top:2983px">Latest Blog</h2>
<div class="blog-img" style="left:90px;background:linear-gradient(180deg,#6c6a64,#3a3936 70%,#5a5a50)" role="img" aria-label="Wall-mounted TV above a console"></div>
<div class="blog-img" style="left:437px;background:linear-gradient(135deg,#f2f2f4,#d7d9de 60%,#9aa0ad)" role="img" aria-label="Technician installing a ceiling camera"></div>
<div class="blog-img" style="left:783px;background:linear-gradient(135deg,#6d7278,#2f3338 60%,#8b8f93)" role="img" aria-label="Disassembled phone parts on a workbench"></div>

<h3 class="blog-title" style="left:89px">Lorem ipsum dolor sit</h3>
<div class="blog-rule" style="left:90px;top:3364px"></div>
<p class="blog-text" style="left:90px;top:3385px">Lorem ipsum dolor sit amet, consectetur aing elit, sed do eiusmod tempor incididunt ut labore et dolore magna aliqua.</p>
<a class="read-more" style="left:90px;top:3481px">Read More »</a>

<h3 class="blog-title" style="left:436px">Lorem ipsum dolor sit</h3>
<div class="blog-rule" style="left:437px;top:3364px"></div>
<p class="blog-text" style="left:437px;top:3385px">Lorem ipsum dolor sit amet, consectetur aing elit, sed do eiusmod tempor incididunt ut labore et dolore magna aliqua.</p>
<a class="read-more" style="left:437px;top:3481px">Read More »</a>

<h3 class="blog-title" style="left:782px">Lorem ipsum dolor sit amet, consectetur adipisc</h3>
<div class="blog-rule" style="left:783px;top:3395px"></div>
<p class="blog-text" style="left:783px;top:3412px">Lorem ipsum dolor sit amet, consectetur aing elit, sed do eiusmod tempor incididunt ut labore</p>
<a class="read-more" style="left:783px;top:3481px">Read More »</a>

<footer class="footer"></footer>
<h4 class="f-head" style="left:90px">RECENT NEWS</h4>
<h4 class="f-head" style="left:367px">USEFULL LINKS</h4>
<h4 class="f-head" style="left:569px">NEWSLETTER</h4>
<h4 class="f-head" style="left:873px">CONTACT US</h4>

<div class="news-thumb" style="left:90px;top:3691px" role="img" aria-label="News author photo"></div>
<div class="f-small" style="left:169px;top:3687px;width:160px">Lorem ipsum dolor sit amet, consectetur<br><span class="news-date">Jan 12,2019</span></div>
<div class="news-thumb" style="left:90px;top:3777px" role="img" aria-label="News author photo"></div>
<div class="f-small" style="left:169px;top:3773px;width:160px">Lorem ipsum dolor sit amet, consectetur<br><span class="news-date">Jan 12,2019</span></div>

<span class="f-link" style="top:3689px">Home</span>
<span class="f-link" style="top:3717px">About Us</span>
<span class="f-link" style="top:3745px">Areas Served</span>
<span class="f-link" style="top:3772px">Pricing and Services</span>
<span class="f-link" style="top:3800px">Contact Us</span>

<div class="f-small" style="left:569px;top:3683px;width:180px;line-height:28px">Lorem ipsum dolor sit amet, consectetur</div>
<div class="f-input">Email Address</div>
<div class="f-send"><svg width="18" height="18" viewBox="0 0 18 18"><path d="M1 8l16-7-6 16-3-6z" fill="#fff"/></svg></div>
<span class="f-social" style="left:581px"></span>
<span class="f-social" style="left:630px"></span>
<span class="f-social" style="left:679px"></span>

<div class="f-small" style="left:873px;top:3683px;width:200px;line-height:28px">Lorem ipsum dolor sit amet, consectetur</div>
<div class="f-rule" style="top:3749px"></div>
<div class="f-row" style="top:3762px"><svg width="10" height="14" viewBox="0 0 10 14"><path d="M5 0a5 5 0 0 1 5 5c0 4-5 9-5 9S0 9 0 5a5 5 0 0 1 5-5z" fill="#fff"/><circle cx="5" cy="5" r="2" fill="#141414"/></svg><span>42 Larkspur Ln, Fenwick,<br>PA 17400</span></div>
<div class="f-rule" style="top:3812px"></div>
<div class="f-row" style="top:3822px"><svg width="12" height="12" viewBox="0 0 24 24"><path d="M6.6 10.8a15 15 0 0 0 6.6 6.6l2.2-2.2a1 1 0 0 1 1-.25 11.4 11.4 0 0 0 3.6.57 1 1 0 0 1 1 1V20a1 1 0 0 1-1 1A17 17 0 0 1 3 4a1 1 0 0 1 1-1h3.5a1 1 0 0 1 1 1c0 1.25.2 2.45.57 3.57a1 1 0 0 1-.25 1z" fill="#fff"/></svg><span>555-014-2280</span></div>
<div class="f-rule" style="top:3853px"></div>
<div class="f-row" style="top:3865px"><svg width="14" height="11" viewBox="0 0 18 14"><rect width="18" height="14" rx="2" fill="#fff"/><path d="M1 1.5l8 6 8-6" stroke="#141414" stroke-width="1.6" fill="none"/></svg><span>hello@vantorim.com</span></div>

<p class="copyright">© Copyrights.2020.The Company name</p>

</body>
</html>
```